Zorvo Salsa label for 16oz jar

We need a design for a label for a 16oz glass jar for salsa (dimensions in inches- 2.75 x9.5). Name of salsa is “Zorvo Salsa” and needs to include a place for medium or hot for the different flavors. Looking for bright Fiesta colors but a mature look. Attached is an image of the coloring scheme we like. There will need to be nutrition facts on one end and a description of the product/flavor on the other side of the label. Ultimately at this point looking for brand design.

```html
<!DOCTYPE html>
<html lang="en">
<head>
<meta charset="utf-8">
<title>Zorvo Salsa – Hot – Jar Label</title>
<link rel="stylesheet" href="https://fonts.googleapis.com/css2?family=Bangers&family=Roboto+Condensed:wght@400;700&display=swap">
<style>
  :root{
    --ink:#0b0b0b;
    --red:#e8262a;
    --orange:#f7941d;
    --yellow:#f9c51b;
    --pink:#ec1c74;
    --green:#6d9c3a;
    --white:#ffffff;
    --display:'Bangers', cursive;
    --body:'Roboto Condensed', Arial, sans-serif;
  }
  *{box-sizing:border-box;margin:0;padding:0}
  html,body{width:1200px;height:347px;overflow:hidden;background:var(--ink)}
  .label{position:relative;width:1200px;height:347px;background:var(--ink);overflow:hidden;font-family:var(--body);color:var(--white)}

  .pattern-band{position:absolute;left:0;width:1200px;background:linear-gradient(180deg,var(--yellow) 0%,var(--red) 55%,var(--red) 100%)}
  .pattern-band.top{top:10px;height:42px}
  .pattern-band.bottom{top:297px;height:40px;background:linear-gradient(0deg,var(--yellow) 0%,var(--red) 55%,var(--red) 100%)}
  .rule{position:absolute;left:0;width:1200px;height:6px;background:var(--orange)}
  .rule.top{top:53px}
  .rule.bottom{top:289px}

  .tagline{position:absolute;left:70px;top:76px;font-family:var(--display);font-size:27px;letter-spacing:.5px;color:var(--yellow);transform:skewX(-8deg)}
  .description{position:absolute;left:70px;top:112px;width:320px;font-family:var(--display);font-size:12.5px;line-height:10.5px;letter-spacing:.3px;color:var(--yellow);transform:skewX(-8deg)}
  .storage{position:absolute;left:71px;top:160px;font-size:15px;font-weight:700;transform:scaleX(.92);transform-origin:left}
  .maker{position:absolute;left:245px;top:230px;font-size:13.5px;line-height:15px;font-weight:700;transform:scaleX(.92);transform-origin:left}

  .art{position:absolute}
  .art.cactus{left:418px;top:80px;width:62px;height:205px;background:var(--red);border-radius:24px 24px 0 0}
  .art.sombrero{left:600px;top:12px;width:262px;height:86px;border-radius:50%/60%;background:linear-gradient(180deg,var(--orange) 0%,var(--red) 70%)}
  .art.peppers{left:500px;top:218px;width:142px;height:62px;border-radius:40px;background:linear-gradient(90deg,#c9181d,var(--red))}

  .brand-name{position:absolute;left:492px;top:96px;font-family:var(--display);font-size:118px;line-height:1;color:var(--pink);letter-spacing:2px}
  .product-type{position:absolute;left:650px;top:226px;font-family:var(--display);font-size:62px;line-height:1;color:var(--yellow);letter-spacing:2px}
  .heat-level{position:absolute;left:806px;top:165px;font-family:var(--display);font-size:30px;color:var(--red);letter-spacing:2px;transform:rotate(-90deg);transform-origin:center}
  .net-weight{position:absolute;left:827px;top:248px;font-size:15px;line-height:16px;font-weight:700}

  .nutrition{position:absolute;left:945px;top:26px;width:163px;height:305px;background:var(--white);color:var(--ink);border:2px solid var(--ink);outline:2px solid var(--white);padding:3px 5px;font-size:8.3px}
  .nutrition .title{font-weight:700;font-size:20.5px;line-height:22px;letter-spacing:-.2px}
  .nutrition .hair{border-top:1px solid var(--ink)}
  .nutrition .thick{border-top:6px solid var(--ink);margin:1px 0}
  .nutrition .mid{border-top:3px solid var(--ink);margin:1px 0}
  .nutrition .servings{font-size:7.5px;margin-top:1px}
  .nutrition .serving-size{display:flex;justify-content:space-between;font-weight:700;font-size:11.5px;line-height:13px}
  .nutrition .amount{font-size:6.8px;font-weight:700}
  .nutrition .calories{display:flex;justify-content:space-between;font-weight:700;font-size:16px;line-height:17px}
  .nutrition .calories span:last-child{font-size:22px;line-height:17px}
  .nutrition .dv-head{text-align:right;font-size:7.5px;font-weight:700;padding:1px 0}
  .nutrition .row{display:flex;justify-content:space-between;border-top:1px solid var(--ink);line-height:11.3px}
  .nutrition .row b{font-weight:700}
  .nutrition .row.indent{padding-left:6px}
  .nutrition .row.indent2{padding-left:6px}
  .nutrition .footnote{font-size:5.5px;line-height:6.6px;margin-top:2px}

  .ingredients{position:absolute;left:1117px;top:320px;width:240px;font-size:6.6px;line-height:7.6px;color:var(--yellow);transform:rotate(-90deg);transform-origin:top left;text-transform:uppercase}
</style>
</head>
<body>
<main class="label">
  <div class="pattern-band top" role="img" aria-label="Decorative zigzag and dot border in red and yellow"></div>
  <div class="rule top"></div>
  <div class="rule bottom"></div>
  <div class="pattern-band bottom" role="img" aria-label="Decorative zigzag and dot border in red and yellow"></div>

  <h2 class="tagline">A Recipe for Double Dippin'!</h2>
  <p class="description">Our hot salsa has the same southwest blend<br>of zesty with the spice level kicked into high gear.<br>Zorvo cautiously!</p>
  <p class="storage">Refrigerate after opening. Best served chilled.</p>
  <p class="maker">Manufactured for:<br>Zorvo Zorvo Salsa, LLC<br>Marlow Springs, KS 66000</p>

  <div class="art cactus" role="img" aria-label="Red saguaro cactus illustration"></div>
  <div class="art sombrero" role="img" aria-label="Colourful sombrero illustration"></div>
  <div class="art peppers" role="img" aria-label="Two red chili peppers illustration"></div>

  <h1 class="brand-name">Zorvo</h1>
  <p class="product-type">SALSA</p>
  <p class="heat-level">HOT</p>
  <p class="net-weight">NET WT.<br>16OZ (453G)</p>

  <section class="nutrition" aria-label="Nutrition Facts">
    <div class="title">Nutrition Facts</div>
    <div class="hair"></div>
    <div class="servings">16 servings per container</div>
    <div class="serving-size"><span>Serving Size</span><span>2 Tbsp (28g)</span></div>
    <div class="thick"></div>
    <div class="amount">Amount Per Serving</div>
    <div class="calories"><span>Calories</span><span>10</span></div>
    <div class="mid"></div>
    <div class="dv-head">% Daily Value*</div>
    <div class="row"><span><b>Total Fat</b> 0g</span><b>0%</b></div>
    <div class="row indent"><span>Saturated Fat 0g</span><b>0%</b></div>
    <div class="row indent"><span>Trans Fat 0g</span><span></span></div>
    <div class="row"><span><b>Cholesterol</b> 0 mg</span><b>0%</b></div>
    <div class="row"><span><b>Sodium</b> 210mg</span><b>9%</b></div>
    <div class="row"><span><b>Total Carbohydrate</b> 2g</span><b>1%</b></div>
    <div class="row indent"><span>Dietary Fiber 0g</span><b>0%</b></div>
    <div class="row indent"><span>Total Sugar &lt;1 g</span><span></span></div>
    <div class="row indent2"><span>Includs 0g Added Sugars</span><b>0%</b></div>
    <div class="row"><span><b>Protein</b> 0g</span><span></span></div>
    <div class="thick"></div>
    <div class="row" style="border-top:0"><span>Vitamin D 0mcg</span><b>0%</b></div>
    <div class="row"><span>Calcium 20mg</span><b>2%</b></div>
    <div class="row"><span>Iron 0,4mg</span><b>2%</b></div>
    <div class="row"><span>Potassium 10mg</span><b>0%</b></div>
    <div class="mid"></div>
    <p class="footnote">* The % Daily Value (DV) tells you how much a nutrient in a serving of food contributes to a daily diet. 2,000 calories a day is used for general nutrition advice.</p>
  </section>

  <p class="ingredients">Ingredients: Diced tomatoes (tomatoes, tomato juice, &lt;2% of: salt, citric acid, calcium chloride), cilantro, jalapeno peppers, cumin, kosher salt, granulated garlic, the juice of fresh limes, dehydrated onion, black pepper, celery salt.</p>
</main>
</body>
</html>
```